Business Card Design Project

Business card design based on the existing logo.

Target Market(s)

Small to medium business owners and CIO's looking for professional IT services.

Industry/Entity Type

Business

Font styles to use
Serif
Sans Serif

Requirements
Must have
• Logo, company name, company details

Text to appear on the business card
Name / Title:
Leon Fairholt
CEO

Address:
Valtiro Limited
Level 3, 42 Kestle St
P O Box 462
Korimako 5391

Other details:
leon@valtiro.co
Ph: 0800 519 308
Mob: +64 21 948 216
www.valtiro.co

Nice to have
• I would look at both single and double sided options. My initial thought is double sided with just the logo with the grey framing for the front and the name and details on the back. But I'm open to other design options.

```html
<!DOCTYPE html>
<html lang="en">
<head>
<meta charset="utf-8">
<title>Valtiro business card</title>
<link rel="stylesheet" href="https://fonts.googleapis.com/css2?family=Open+Sans:wght@400;600;700&display=swap">
<style>
  :root {
    --page: #e4e7ea;
    --card-white: #fbfbfa;
    --ink: #2a2c2e;
    --brand-blue: #1c5878;
    --brand-teal: #1f8fa0;
    --back-deep: #15587a;
    --muted: #8c8f92;
    --icon-grey: #9a9c9e;
    --rule: #1c5878;
  }
  * { box-sizing: border-box; margin: 0; padding: 0; }
  html, body {
    width: 1200px; height: 800px; overflow: hidden;
    background: var(--page);
    font-family: "Open Sans", Arial, sans-serif;
  }
  .canvas {
    position: relative; width: 1200px; height: 800px;
    display: flex; flex-direction: column; align-items: center; justify-content: center; gap: 32px;
  }
  .card {
    position: relative; width: 616px; height: 352px;
    box-shadow: 0 6px 18px rgba(0,0,0,.18);
    overflow: hidden;
  }
  .card--front { background: var(--card-white); color: var(--ink); }
  .card--back {
    background: linear-gradient(135deg, var(--back-deep) 0%, var(--brand-teal) 100%);
    display: flex; align-items: center; justify-content: center;
  }

  .holder { position: absolute; top: 26px; right: 34px; text-align: right; }
  .holder__name { font-size: 22px; font-weight: 700; color: var(--brand-blue); line-height: 1.1; }
  .holder__title { font-size: 12px; color: var(--muted); margin-top: 2px; }

  .brand { position: absolute; top: 148px; right: 34px; display: flex; align-items: center; gap: 10px; }
  .brand__dot { width: 18px; height: 18px; border-radius: 50%; background: var(--brand-blue); }
  .brand__name { font-size: 40px; font-weight: 400; color: var(--ink); letter-spacing: .5px; line-height: 1; }

  .web {
    position: absolute; top: 220px; right: 34px;
    font-size: 14px; font-weight: 700; color: var(--brand-blue); line-height: 20px;
  }
  .web-rule { position: absolute; top: 242px; left: 34px; right: 34px; height: 1.5px; background: var(--rule); }

  .address {
    position: absolute; left: 34px; top: 250px;
    font-size: 14px; line-height: 19px; font-style: normal;
  }
  .address__company { color: var(--brand-blue); font-weight: 600; }

  .contact-rule { position: absolute; top: 312px; left: 34px; width: 300px; height: 1px; background: var(--rule); }

  .contacts__item { display: flex; align-items: center; gap: 6px; font-size: 13px; line-height: 20px; }
  .contacts__icon {
    width: 20px; height: 20px; border-radius: 50%; background: var(--icon-grey);
    display: flex; align-items: center; justify-content: center; flex: none;
  }
  .contacts__mobile { position: absolute; top: 252px; left: 340px; }
  .contacts {
    position: absolute; left: 34px; top: 320px;
    display: flex; gap: 18px; align-items: center;
  }

  .back-brand { color: #fff; font-size: 56px; font-weight: 400; letter-spacing: 1px; display: flex; align-items: center; gap: 14px; }
  .back-brand__dot { width: 24px; height: 24px; border-radius: 50%; background: #fff; }
</style>
</head>
<body>
<main class="canvas">
  <section class="card card--front" aria-label="Business card front">
    <div class="holder">
      <p class="holder__name">Leon Fairholt</p>
      <p class="holder__title">CEO</p>
    </div>

    <div class="brand">
      <span class="brand__dot"></span>
      <span class="brand__name">Valtiro</span>
    </div>

    <p class="web">www.valtiro.co</p>
    <div class="web-rule"></div>

    <address class="address">
      <p class="address__company">Valtiro Limited</p>
      <p>Level 3, 42 Kestle St</p>
      <p>P O Box 462 | Korimako 5391</p>
    </address>

    <span class="contacts__item contacts__mobile">
      <span class="contacts__icon">
        <svg width="8" height="12" viewBox="0 0 8 12"><rect x=".5" y=".5" width="7" height="11" rx="1" fill="none" stroke="#fff"/><rect x="2" y="2" width="4" height="6" fill="#fff"/></svg>
      </span>+64 21 948 216
    </span>

    <div class="contact-rule"></div>
    <div class="contacts">
      <span class="contacts__item">
        <span class="contacts__icon">
          <svg width="12" height="9" viewBox="0 0 12 9"><rect x=".5" y=".5" width="11" height="8" fill="none" stroke="#fff"/><path d="M.5 .5 6 5l5.5-4.5" fill="none" stroke="#fff"/></svg>
        </span>leon@valtiro.co
      </span>
      <span class="contacts__item">
        <span class="contacts__icon">
          <svg width="11" height="11" viewBox="0 0 12 12"><path d="M2.5 1 4.5 3.5 3.4 4.8c.8 1.6 2.2 3 3.8 3.8L8.5 7.5 11 9.5 9.8 11C5 10.6 1.4 7 1 2.2Z" fill="#fff"/></svg>
        </span>0800 519 308
      </span>
    </div>
  </section>

  <section class="card card--back" aria-label="Business card back">
    <div class="back-brand">
      <span class="back-brand__dot"></span>
      <span>Valtiro</span>
    </div>
  </section>
</main>
</body>
</html>
```